Billboard

I am a landscaping and irrigation company. I have purchased a billboard in a good part of town and I want a billboard that will stand out and show both colorful plantings/flowers and irrigation. My website is www.gardenvane.me

A phrase I have that of is showers and flowers, but I am not sure how to illustrate that since most stock pics are of just sprinkler heads and grass.

Target Market(s)

Target market is wealthy women

Industry/Entity Type

Landscaping

Requirements
Should not have
• Needs to look sharp and professional.

```html
<!DOCTYPE html>
<html lang="en">
<head>
<meta charset="utf-8">
<title>GardenVane Billboard</title>
<link rel="stylesheet" href="https://fonts.googleapis.com/css2?family=Arimo:wght@400;700&family=Roboto+Condensed:wght@400;700&display=swap">
<style>
  :root {
    --navy: #020b45;
    --white: #ffffff;
    --green: #1f9a1c;
    --lime: #5be63a;
    --yellow: #fff700;
    --ink: #0a0a0a;
    --grey: #4e4e4e;
  }
  * { margin: 0; padding: 0; box-sizing: border-box; }
  html, body { width: 1200px; height: 634px; overflow: hidden; background: var(--navy); }
  .canvas { position: relative; width: 1200px; height: 634px; background: var(--navy); }
  .billboard {
    position: absolute; left: 79px; top: 72px; width: 1036px; height: 489px;
    background: var(--white); overflow: hidden;
  }
  .garden-photo {
    position: absolute; left: 0; top: 0; width: 800px; height: 489px;
    background:
      radial-gradient(ellipse 180px 120px at 560px 300px, rgba(214,70,200,.75), transparent 70%),
      radial-gradient(ellipse 160px 100px at 330px 420px, rgba(205,25,40,.6), transparent 70%),
      radial-gradient(ellipse 260px 160px at 430px 340px, rgba(40,130,30,.9), transparent 75%),
      radial-gradient(ellipse 220px 120px at 80px 400px, rgba(30,40,25,.85), transparent 75%),
      linear-gradient(180deg, #e8eef0 0%, #d9b8d6 25%, #b56fb5 45%, #3f8a2a 70%, #2a5a1e 100%);
    -webkit-mask-image: linear-gradient(90deg, #000 0%, #000 72%, transparent 100%);
    mask-image: linear-gradient(90deg, #000 0%, #000 72%, transparent 100%);
  }
  .headline {
    position: absolute; left: 38px; top: 30px;
    font-family: "Arimo", Arial, sans-serif; font-weight: 400;
    font-size: 86px; line-height: 82px; color: var(--ink); letter-spacing: -1.5px;
  }
  .headline strong { font-weight: 700; }
  .call-tab {
    position: absolute; left: 651px; top: 0; width: 370px; height: 50px;
    background: var(--green); border-radius: 0 0 0 16px;
    display: flex; align-items: center; justify-content: center;
    font-family: "Roboto Condensed", "Arial Narrow", sans-serif; font-weight: 700;
    font-size: 31px; color: var(--white);
  }
  .services {
    position: absolute; left: 701px; top: 97px; list-style: none;
    font-family: "Roboto Condensed", "Arial Narrow", sans-serif; font-weight: 400;
    font-size: 33px; color: var(--grey);
  }
  .services li { height: 45px; display: flex; align-items: center; }
  .services li::before {
    content: ""; width: 12px; height: 12px; background: var(--green);
    margin-right: 16px; flex: none;
  }
  .wave { position: absolute; left: 0; top: 0; }
  .brand {
    position: absolute; left: 711px; top: 378px; width: 280px;
    display: flex; flex-direction: column; align-items: center;
    font-family: "Arimo", Arial, sans-serif; color: var(--ink);
  }
  .brand-name { font-weight: 700; font-size: 36px; line-height: 42px; }
  .brand-web { font-weight: 400; font-size: 17px; line-height: 22px; margin-top: 4px; }
</style>
</head>
<body>
<div class="canvas">
  <div class="billboard">
    <div class="garden-photo" role="img" aria-label="Pop-up sprinkler spraying water over a bed of pink, purple and red flowers"></div>
    <h1 class="headline">Showers<br>and <strong>Flowers</strong></h1>
    <div class="call-tab">Call Now : (478) 555-0147</div>
    <ul class="services">
      <li>Landscaping</li>
      <li>Lawn Care Services</li>
      <li>Landscape Lighting</li>
      <li>Stone Work</li>
      <li>Sprinkler Systems</li>
    </ul>
    <svg class="wave" width="1036" height="489" viewBox="0 0 1036 489" aria-hidden="true">
      <path d="M0 414 C 150 455, 260 462, 420 430 C 600 392, 760 330, 1036 340 L1036 489 L0 489 Z" fill="var(--lime)"/>
      <path d="M0 434 C 150 465, 260 470, 430 440 C 610 405, 770 342, 1036 350 L1036 489 L0 489 Z" fill="var(--yellow)"/>
    </svg>
    <div class="brand">
      <div class="brand-name">GardenVane</div>
      <div class="brand-web">www.gardenvane.me</div>
    </div>
  </div>
</div>
</body>
</html>
```